Brightkoru NZ Brand, Revenue, Promotions & Events

I need an innovative business card that pops my brand. I like the colours against darker gradients and i'm not afraid to be bold.

I run my own Business, Brand, Event & Promotion company. I specialise in breathing life into businesses and adding atmosphere to promotions and events. I am concept based lady that likes to test the boundaries and create stand out campaigns that connect with the consumer.

I have 12 years business experience in a realm of interesting fields form 11 years in coordinating international music festivals & promotions, 6 years in radio with 8 radio awards including a NZ radio award for best sales team in NZ and was the national brand and sales manager for New Zealands 1st indoor entertainment mall. With 10 years of experience in advertising sales, I have an eye for creating revenue streams for businesses and thrive on implementing campaigns that compliment those streams.

I love sayings like "Do what you love, love what you do" and believe that you can achieve anything you want.

I have been fortunate in my career that my connections have carried me without needing to promote my business however it is important that I start to do so.

Target Market(s)

Decision makers 25 to 54

Contact Information for Business Card

Petra Holsworth
Director
p. 022 739 5081
e. petra@brightkoru.example
www.brightkoru.example

FB, IG and Linkedin logo

Font styles to use
Sans Serif

Colors

Designer to choose colors to be used in the design.

Requirements
Must have
• Petra Holsworth
• Director
• p. 022 739 5081
• e. petra@brightkoru.example
• www.brightkoru.example
• FB, IG and Linkedin logo
Nice to have
• I am looking for a business card with character, that leaves my presence with my customer and makes them remember my brand & optimistic personality when i walk out the door.

```html
<!DOCTYPE html>
<html lang="en">
<head>
<meta charset="utf-8">
<title>Brightkoru NZ — Business Card</title>
<link href="https://fonts.googleapis.com/css2?family=Montserrat:wght@400;600;700&display=swap" rel="stylesheet">
<style>
  :root {
    --backdrop: #dcdcda;
    --card: #2f2f31;
    --accent: #27a7e0;
    --muted: #9a9ca0;
    --deboss: #252527;
    --deboss-text: #404043;
  }
  * { margin: 0; padding: 0; box-sizing: border-box; }
  html, body { width: 1200px; height: 801px; overflow: hidden; }
  body {
    background: var(--backdrop);
    font-family: "Montserrat", sans-serif;
    position: relative;
  }
  .card {
    position: absolute;
    top: 246px;
    width: 540px;
    height: 309px;
    background: var(--card);
    border-bottom: 3px solid var(--accent);
    border-right: 2px solid var(--accent);
  }
  .card--front { left: 40px; }
  .card--back { left: 620px; }

  .brand {
    position: absolute;
    left: 34px;
    top: 128px;
  }
  .brand__name {
    display: flex;
    align-items: center;
    gap: 8px;
    font-weight: 700;
    font-size: 30px;
    letter-spacing: 1px;
    color: var(--accent);
    line-height: 1;
  }
  .brand__dot {
    width: 14px; height: 14px; border-radius: 50%;
    background: var(--accent);
  }
  .brand__tagline {
    margin-top: 6px;
    font-size: 9.5px;
    letter-spacing: 0.4px;
    color: var(--muted);
    text-transform: uppercase;
  }

  .divider {
    position: absolute;
    left: 300px;
    top: 70px;
    width: 1.5px;
    height: 170px;
    background: var(--accent);
  }

  .contact {
    position: absolute;
    left: 320px;
    top: 78px;
  }
  .contact__name {
    font-weight: 700;
    font-size: 21px;
    color: var(--accent);
  }
  .contact__role {
    font-size: 14px;
    color: var(--muted);
    margin-bottom: 14px;
  }
  .contact__list { list-style: none; }
  .contact__item {
    display: flex;
    align-items: center;
    gap: 8px;
    font-size: 13px;
    color: var(--muted);
    margin-bottom: 5px;
  }
  .contact__icon { width: 11px; height: 11px; flex: none; }

  .social {
    position: absolute;
    right: 16px;
    top: 14px;
    display: flex;
    gap: 4px;
  }
  .social__tile {
    width: 14px; height: 14px;
    border-radius: 2px;
    background: var(--accent);
  }

  .card--back { background: var(--card); }
  .deboss {
    position: absolute;
    left: 0; right: 0;
    top: 112px;
    text-align: center;
  }
  .deboss__name {
    display: inline-flex;
    align-items: center;
    gap: 10px;
    font-weight: 700;
    font-size: 40px;
    letter-spacing: 2px;
    color: var(--deboss-text);
  }
  .deboss__dot {
    width: 18px; height: 18px; border-radius: 50%;
    background: var(--deboss-text);
  }
  .deboss__tagline {
    margin-top: 8px;
    font-size: 12.5px;
    letter-spacing: 0.6px;
    color: var(--deboss-text);
    text-transform: uppercase;
  }
</style>
</head>
<body>
  <section class="card card--front" aria-label="Business card front">
    <div class="social" aria-label="Social media">
      <span class="social__tile" title="Social profile"></span>
      <span class="social__tile" title="Social profile"></span>
      <span class="social__tile" title="Social profile"></span>
    </div>

    <div class="brand">
      <div class="brand__name"><span class="brand__dot"></span>Brightkoru NZ</div>
      <div class="brand__tagline">Brand | Revenue | Events &amp; Promotions</div>
    </div>

    <div class="divider"></div>

    <div class="contact">
      <div class="contact__name">Petra Holsworth</div>
      <div class="contact__role">Director</div>
      <ul class="contact__list">
        <li class="contact__item">
          <svg class="contact__icon" viewBox="0 0 12 12" aria-hidden="true"><path fill="#27a7e0" d="M2.5 1 4.5 1 5.3 3.6 4 4.6C4.7 6 6 7.3 7.4 8L8.4 6.7 11 7.5 11 9.5C11 10.3 10.3 11 9.5 11 5 11 1 7 1 2.5 1 1.7 1.7 1 2.5 1Z"/></svg>
          022 739 5081
        </li>
        <li class="contact__item">
          <svg class="contact__icon" viewBox="0 0 12 12" aria-hidden="true"><rect x="0.5" y="2.5" width="11" height="7.5" rx="1" fill="#27a7e0"/><path d="M1 3.2 6 6.8 11 3.2" stroke="#2f2f31" stroke-width="1" fill="none"/></svg>
          petra@brightkoru.example
        </li>
        <li class="contact__item">
          <svg class="contact__icon" viewBox="0 0 12 12" aria-hidden="true"><circle cx="6" cy="6" r="5.2" fill="#27a7e0"/><path d="M1 6H11M6 1C4 3.5 4 8.5 6 11M6 1C8 3.5 8 8.5 6 11" stroke="#2f2f31" stroke-width="0.8" fill="none"/></svg>
          www.brightkoru.example
        </li>
      </ul>
    </div>
  </section>

  <section class="card card--back" aria-label="Business card back">
    <div class="deboss">
      <div class="deboss__name"><span class="deboss__dot"></span>Brightkoru NZ</div>
      <div class="deboss__tagline">Brand | Revenue | Events &amp; Promotions</div>
    </div>
  </section>
</body>
</html>
```